Quibont homepage

Re-design www.quibont-example.com. Visitors are developers and CTOs. Something simple and straightforward. Need different and special landingpage.
I like this page: http://melvantry-example.io/ (service is also similar).
Logo is at http://www.quibont-example.com/quibont.svg
Be bold with content you see on www.quibont-example.com.
If you want ... make main message shorter, add links that doesn't exist, remove something etc.
Landing page should be cleaner than it is now.
Things what I want to have on page (missing on quibont-example.com):
- testimonials
- contact form (can be simple as "send us e-mail...")
Quibont supports Tavix, Brimhollow, Fenlow and Korvet. You are welcome to use logos for those databases.
CTO-s and developers/programmers
It Service

```html
<!DOCTYPE html>
<html lang="en">
<head>
<meta charset="utf-8">
<title>Quibont</title>
<link rel="stylesheet" href="https://fonts.googleapis.com/css2?family=Philosopher:ital@0;1&family=Yanone+Kaffeesatz:wght@400&family=Open+Sans:wght@500&display=swap">
<style>
  :root {
    --cyan: #27b3e6;
    --ink: #1a2118;
    --panel-a: #7f9a78;
    --panel-b: #a9b9a0;
    --gold: #e8b330;
    --night: #070707;
    --orange: #ea8a24;
    --fb: #3b5998;
    --tw: #2fa3dc;
    --gp: #d8462e;
    --white: #ffffff;
  }
  html, body { margin: 0; padding: 0; overflow: hidden; }
  body { width: 826px; height: 1200px; background: var(--white); position: relative; }
  .feature {
    position: absolute; left: 0; width: 826px; height: 386px; overflow: hidden;
    background: linear-gradient(160deg, var(--panel-a) 0%, var(--panel-b) 45%, var(--panel-a) 100%);
    font-family: "Philosopher", sans-serif; font-style: italic; color: var(--ink);
  }
  .feature-data { top: 0; }
  .feature-conf { top: 403px; }
  .feature-title {
    position: absolute; left: 0; width: 100%; text-align: center; margin: 0;
    font-family: "Philosopher", sans-serif; font-style: normal; font-weight: 400;
    font-size: 33px; color: var(--cyan);
  }
  .feature-body { position: absolute; margin: 0; font-size: 37px; line-height: 47px; }
  .feature-data .feature-title { top: 28px; }
  .feature-data .feature-body { top: 90px; left: 0; width: 100%; text-align: center; }
  .feature-conf .feature-title { top: 44px; }
  .feature-conf .feature-body { top: 108px; left: 45px; }
  .feature-conf .feature-body span { display: block; padding-left: 11px; }
  .feature-conf .feature-body span.lead { padding-left: 0; }
  .read-more { font-size: 23px; font-style: normal; margin-left: 26px; }
  .cta {
    position: absolute; left: 209px; top: 828px; width: 380px; height: 66px;
    background: var(--gold); color: var(--night); text-align: center;
    font-family: "Open Sans", sans-serif; font-weight: 500; font-size: 31px; line-height: 66px;
    text-decoration: none;
  }
  .footer { position: absolute; left: 0; top: 921px; width: 826px; height: 279px; background: var(--night); }
  .footer-nav { position: absolute; left: 24px; top: 36px; font-family: "Yanone Kaffeesatz", sans-serif; font-size: 37px; }
  .footer-nav a { color: var(--cyan); text-decoration: none; margin-right: 12px; }
  .social { position: absolute; left: 599px; top: 25px; }
  .footer-rule { position: absolute; left: 0; top: 199px; width: 826px; height: 8px; background: var(--orange); }
  .footer-mail {
    position: absolute; left: 0; top: 222px; width: 100%; text-align: center;
    font-family: "Philosopher", sans-serif; font-size: 35px; color: var(--cyan); text-decoration: none;
  }
</style>
</head>
<body>
  <section class="feature feature-data" role="img" aria-label="Background photo of a developer at a desk, tinted green">
    <h2 class="feature-title">Data Manipulation</h2>
    <p class="feature-body">To rules defined in database configuration<br>and data&nbsp; sent as objects in array.<br>Sending one row JSON means send[{id:1,foo:2}],<br>just {id:1, foo:2}.<span class="read-more">Read More</span></p>
  </section>

  <section class="feature feature-conf" role="img" aria-label="Background photo of a workspace with a laptop, tinted green">
    <h2 class="feature-title">Global conf</h2>
    <p class="feature-body"><span class="lead">Global configuration file is used for configuring:</span><span>server configurations</span><span>database connections</span><span>static file directory</span><span>template directory<span class="read-more" style="display:inline;padding:0">Read More</span></span></p>
  </section>

  <a class="cta" href="#">Gets Started Free</a>

  <footer class="footer">
    <nav class="footer-nav">
      <a href="#">Blog</a><a href="#">Press</a><a href="#">FAQ</a><a href="#">About</a><a href="#">Contact</a>
    </nav>
    <svg class="social" width="210" height="66" viewBox="0 0 210 66" aria-label="Social links">
      <circle cx="33" cy="33" r="31" fill="var(--fb)"/>
      <circle cx="107" cy="33" r="31" fill="var(--tw)"/>
      <circle cx="180" cy="33" r="31" fill="var(--gp)"/>
    </svg>
    <div class="footer-rule"></div>
    <a class="footer-mail" href="mailto:info@quibont-example.com">info@quibont-example.com</a>
  </footer>
</body>
</html>
```